Pinecrest Premier Motors *

Professional business cards for our auto wholesale dealership.

Target Market(s)

New and used cars sales managers and middle class to higher end private party buyers.

Industry/Entity Type

Automotive

Contact Information for Business Card

Pinecrest Premier Motors
Marcus T Holloran
Owner
(555) 014-3862
pineprem@mailvista.example
Dealer Lic # 48265

Logo Text

Pinecrest Premier Motors, Pine Prem Motors, PPM, etc

Font styles to use
Serif
Sans Serif

Colors

Designer to choose colors to be used in the design.

Requirements
Must have
• A professional, but not pretentious, look
Nice to have
• It might be nice to see "PPM" in a shape form i.e. circle, triangle, etc in the corner or background somehwere
Should not have
• bright "girly" colors

```html
<!DOCTYPE html>
<html lang="en">
<head>
<meta charset="utf-8">
<title>Pinecrest Premier Motors – Business Card</title>
<link rel="stylesheet" href="https://fonts.googleapis.com/css2?family=Open+Sans:wght@400;600&display=swap">
<style>
  :root {
    --backdrop: #d9d6d1;
    --card-black: #0b0c0e;
    --card-charcoal: #1c1f24;
    --brand-blue: #3b5ec9;
    --muted-grey: #a9adb3;
    --text-white: #f2f3f5;
    --silver-light: #f4f5f7;
    --silver-dark: #6e737a;
  }
  * { margin: 0; padding: 0; box-sizing: border-box; }
  html, body {
    width: 1200px; height: 784px; overflow: hidden;
    background: var(--backdrop);
    font-family: "Open Sans", Arial, sans-serif;
  }
  .canvas { position: relative; width: 1200px; height: 784px; }
  .card {
    position: absolute;
    width: 580px; height: 331px;
    border-radius: 4px;
    overflow: hidden;
    box-shadow: 0 10px 30px rgba(0,0,0,0.25);
  }
  .card--back { left: 60px; top: 60px; }
  .card--front { left: 560px; top: 393px; }
  .card-surface {
    position: absolute; inset: 0;
    background: radial-gradient(ellipse at 50% 30%, var(--card-charcoal) 0%, var(--card-black) 75%);
  }
  .brand {
    position: absolute; left: 0; right: 0;
    display: flex; align-items: center; justify-content: center; gap: 12px;
    color: var(--brand-blue);
    font-weight: 600;
    letter-spacing: 0.02em;
    white-space: nowrap;
  }
  .brand-dot {
    width: 14px; height: 14px; border-radius: 50%;
    background: var(--brand-blue);
  }
  .card--back .brand { top: 140px; font-size: 30px; }
  .card--front .brand { top: 70px; font-size: 26px; }
  .silver-rule {
    position: absolute; left: 0; top: 150px;
    width: 100%; height: 4px;
    background: linear-gradient(90deg, var(--silver-dark) 0%, var(--silver-light) 35%, var(--silver-light) 65%, var(--silver-dark) 100%);
  }
  .lower-panel {
    position: absolute; left: 0; right: 0; top: 154px; bottom: 0;
    background: linear-gradient(180deg, #15171b 0%, var(--card-black) 100%);
  }
  .contact {
    position: absolute; left: 0; right: 0; top: 172px;
    text-align: center;
  }
  .contact-name { color: var(--brand-blue); font-size: 20px; font-weight: 600; line-height: 1.2; }
  .contact-role { color: var(--muted-grey); font-size: 13px; line-height: 1.5; margin-bottom: 8px; }
  .contact-phone { color: var(--brand-blue); font-size: 22px; letter-spacing: 0.12em; line-height: 1.2; }
  .contact-line { color: var(--text-white); font-size: 14px; line-height: 1.45; }
</style>
</head>
<body>
<main class="canvas">
  <section class="card card--back" aria-label="Card back">
    <div class="card-surface" role="img" aria-label="Dark perforated carbon texture"></div>
    <div class="brand"><span class="brand-dot"></span>Pinecrest Premier Motors</div>
  </section>

  <section class="card card--front" aria-label="Card front">
    <div class="card-surface" role="img" aria-label="Dark perforated carbon texture"></div>
    <div class="brand"><span class="brand-dot"></span>Pinecrest Premier Motors</div>
    <div class="lower-panel"></div>
    <div class="silver-rule"></div>
    <div class="contact">
      <p class="contact-name">Marcus T Holloran</p>
      <p class="contact-role">Owner</p>
      <p class="contact-phone">(555) 014-3862</p>
      <p class="contact-line">pineprem@mailvista.example</p>
      <p class="contact-line">Dealer Lic # 48265</p>
    </div>
  </section>
</main>
</body>
</html>
```